Vantrell Law Letterhead

We need a new letterhead design for a Law Firm. The address for the law firm is 4817 Larkspur Boulevard, Suite 250, Houston, Texas 77342. Phone Number: 832-619-3057; Fax Number: 832-407-1694. The logo is uploaded to the project.

```html
<!DOCTYPE html>
<html lang="en">
<head>
<meta charset="utf-8">
<title>Vantrell Law Letterhead</title>
<link href="https://fonts.googleapis.com/css2?family=Arimo:wght@400;700&display=swap" rel="stylesheet">
<style>
  :root {
    --navy: #1f2f5c;
    --red: #c01f2b;
    --ink: #2b2b2b;
    --muted: #555a63;
    --paper: #ffffff;
    --backdrop: #ecedef;
  }
  * { box-sizing: border-box; margin: 0; padding: 0; }
  html, body { width: 1200px; height: 795px; overflow: hidden; }
  body {
    background: var(--backdrop);
    font-family: "Arimo", Arial, sans-serif;
    color: var(--ink);
    position: relative;
  }
  .letterhead {
    position: absolute;
    left: 330px; top: 15px;
    width: 540px; height: 765px;
    background: var(--paper);
    box-shadow: 0 2px 10px rgba(0,0,0,0.12);
  }
  .edge-mark { position: absolute; }
  .edge-mark--navy { left: 0; top: 236px; width: 5px; height: 30px; background: var(--navy); }
  .edge-mark--red { right: 0; top: 22px; width: 5px; height: 30px; background: var(--red); }

  .brand { position: absolute; left: 46px; top: 54px; display: flex; align-items: center; gap: 8px; }
  .brand__square { width: 22px; height: 22px; background: var(--navy); }
  .brand__text { display: flex; flex-direction: column; }
  .brand__name { font-size: 21px; font-weight: 700; color: var(--navy); letter-spacing: 0.5px; line-height: 1; }
  .brand__tagline { margin-top: 4px; padding-top: 3px; border-top: 1px solid var(--red); font-size: 5px; letter-spacing: 0.6px; color: var(--red); text-transform: uppercase; }

  .contact { position: absolute; right: 40px; top: 48px; display: flex; gap: 9px; font-size: 8px; line-height: 1.45; }
  .contact__address { text-align: right; color: var(--ink); }
  .contact__divider { width: 1px; background: var(--red); }
  .contact__lines { list-style: none; }
  .contact__lines li { display: flex; align-items: center; gap: 4px; }
  .contact__lines svg { width: 7px; height: 7px; fill: var(--red); }

  .letter { position: absolute; left: 60px; top: 190px; width: 420px; font-size: 9px; line-height: 1.55; color: var(--muted); }
  .letter__greeting { font-size: 13px; color: var(--ink); margin-bottom: 12px; }
  .letter p { margin-bottom: 12px; text-align: left; }
  .letter__closing { margin-top: 6px; }
  .letter__signature { display: block; margin-top: 6px; width: 70px; height: 26px; background: linear-gradient(90deg, #e6e8ee, #f4f5f8); border-radius: 3px; }
</style>
</head>
<body>
  <main class="letterhead">
    <span class="edge-mark edge-mark--navy"></span>
    <span class="edge-mark edge-mark--red"></span>

    <header>
      <div class="brand">
        <span class="brand__square"></span>
        <div class="brand__text">
          <span class="brand__name">Vantrell Law</span>
          <span class="brand__tagline">Your Injury &amp; Personal Attorneys</span>
        </div>
      </div>

      <div class="contact">
        <address class="contact__address" style="font-style:normal">
          4817 Larkspur Boulevard<br>
          Suite 250<br>
          Houston, Texas 77342
        </address>
        <span class="contact__divider"></span>
        <ul class="contact__lines">
          <li><svg viewBox="0 0 10 10"><path d="M2 0.5 L3.8 0.5 L4.3 3 L3 3.8 Q4 6 6.2 7 L7 5.7 L9.5 6.2 L9.5 8 Q9.5 9.5 8 9.5 Q0.5 9 0.5 2 Q0.5 0.5 2 0.5Z"/></svg>832-619-3057</li>
          <li><svg viewBox="0 0 10 10"><rect x="2.5" y="0.5" width="5" height="3"/><rect x="0.5" y="3.5" width="9" height="4.5" rx="1"/><rect x="2.5" y="7" width="5" height="2.5"/></svg>832-407-1694</li>
          <li><svg viewBox="0 0 10 10"><circle cx="5" cy="5" r="4.5"/></svg>vantrelllaw.com</li>
        </ul>
      </div>
    </header>

    <article class="letter">
      <p class="letter__greeting">Dear Mr. Harlan,</p>
      <p>Lorem ipsum dolor sit amet, consectetur adipiscing elit. Donec orci purus, luctus vitae dignissim eu, iaculis sed purus. Vivamus faucibus, ipsum nec aliquet viverra, leo mauris condimentum ligula, sit amet sagittis enim ligula quis arcu. Nam egestas tortor id nisi porttitor mattis. In tortor ante, ultricies in suscipit a, tempus non massa. Vivamus et auctor mi. Fusce vel massa nulla. Phasellus nec eros mauris, et scelerisque orci.</p>
      <p>Donec malesuada orci vitae nulla accumsan porta a id massa. Quisque accumsan iaculis magna sit amet fringilla. Maecenas consequat, magna eget tincidunt semper, odio nibh rutrum mi, id feugiat ante nisl eu risus. Vestibulum nunc orci, rhoncus a placerat in, ultricies in mi. Cras mattis varius eros, vel fringilla nisi suscipit eget. Quisque scelerisque sagittis nulla at porttitor.</p>
      <p>Sed id augue vitae urna euismod commodo aliquet a quam. Pellentesque arcu velit, cursus et malesuada ut, consequat et diam. Nullam erat sem, rhoncus id ullamcorper vitae, rhoncus et arcu. In ultricies ultricies nulla, ut rutrum nisl iaculis at. Donec eu magna a metus ornare faucibus. Fusce aliquet faucibus ultricies. Morbi semper, est id tincidunt gravida, sem arcu adipiscing lacus, ac bibendum nulla leo eu purus. Quisque nec diam sed risus consectetur accumsan quis quis nibh. Vestibulum id purus lorem.</p>
      <p class="letter__closing">Sincerely,</p>
      <span class="letter__signature" role="img" aria-label="Handwritten signature of the sender"></span>
    </article>
  </main>
</body>
</html>
```